Bramble Wren Childcare centre needs a new LED outdoor banner

We need a new outdoor banner for our pre-school. It needs to be around 2440 mm x 1220 mm. It will be lit at night so I need it to stand out. I'm looking for a modern upbeat design. It will have my logo in the middle which is a graduation teddy bear with our name and phone number on it. I'm happy to experiment with different design options as mine is 20 years old. It needs to be colorful, inviting and very "in your face" and child friendly. It will be located near the fence of the property so it will be seen by cars driving by at a speed of around 50KM/H. So it needs to be clear, big bold fonts and bright colors. Thank you!

```html
<!DOCTYPE html>
<html lang="en">
<head>
<meta charset="UTF-8">
<title>Bramble Wren Childcare – Outdoor Banner</title>
<link href="https://fonts.googleapis.com/css2?family=Fredoka:wght@500;600;700&display=swap" rel="stylesheet">
<style>
  :root {
    --bg: #3a3a3a;
    --banner: #ffffff;
    --ray: #c9ecfb;
    --pink: #e8178f;
    --blue: #13aee8;
    --tan: #c99a74;
  }
  * { margin: 0; padding: 0; box-sizing: border-box; }
  html, body { width: 1200px; height: 759px; overflow: hidden; background: var(--bg); }
  .canvas { position: relative; width: 1200px; height: 759px; }
  .banner {
    position: absolute; left: 40px; top: 100px; width: 1120px; height: 560px;
    background: radial-gradient(ellipse at 50% 55%, var(--banner) 0%, var(--banner) 35%, var(--ray) 100%);
    overflow: hidden; font-family: "Fredoka", sans-serif;
  }
  .crayons-left {
    position: absolute; left: 0; top: 0; width: 135px; height: 560px;
    background: linear-gradient(180deg, #f5d327 0%, #3fb6e3 8%, #5fb33a 16%, #f08a1e 24%, #e3283a 32%, #8f3aa0 40%, #e02b8a 48%, #2b2f86 56%, #7a4a2a 64%, #8dc63f 72%, #f5d327 78%, #3fb6e3 84%, #3aa84a 90%, #f08a1e 95%, #e3283a 100%);
  }
  .pencils-right {
    position: absolute; right: 0; top: 0; width: 145px; height: 560px;
    background: linear-gradient(180deg, #f2a33a 0%, #3c9be3 8%, #33a84a 16%, #f0622a 24%, #e3202a 32%, #8a2a90 40%, #e0237f 48%, #1f1f6e 56%, #6e4424 64%, #7cba3c 72%, #f2a33a 78%, #3c9be3 84%, #33a84a 90%, #f0622a 95%, #e3202a 100%);
  }
  .headline {
    position: absolute; left: 135px; right: 145px; top: 40px;
    text-align: center; color: var(--pink); font-weight: 700; font-size: 96px; line-height: 1;
  }
  .mark {
    position: absolute; left: 462px; top: 170px; width: 196px; height: 196px;
    border-radius: 50%; background: var(--tan);
  }
  .cloud { position: absolute; width: 210px; height: 122px; }
  .cloud svg { position: absolute; inset: 0; }
  .cloud p {
    position: absolute; inset: 0; display: flex; flex-direction: column; justify-content: center; align-items: center;
    color: var(--blue); font-weight: 600; font-size: 30px; line-height: 1.05; text-align: center; padding-top: 8px;
  }
  .cloud-hours { left: 168px; top: 232px; }
  .cloud-ages { left: 744px; top: 230px; }
  .title {
    position: absolute; left: 135px; right: 145px; top: 372px;
    text-align: center; color: var(--blue); font-weight: 600; font-size: 118px; line-height: 1; letter-spacing: 3px;
  }
  .phone {
    position: absolute; left: 360px; top: 483px; width: 400px; height: 60px;
    border: 3px solid var(--pink); border-radius: 30px; background: var(--banner);
    color: var(--pink); font-weight: 600; font-size: 44px; line-height: 54px; text-align: center; letter-spacing: 1px;
  }
</style>
</head>
<body>
<div class="canvas">
  <section class="banner">
    <div class="crayons-left" role="img" aria-label="Row of colourful wax crayons pointing inward"></div>
    <div class="pencils-right" role="img" aria-label="Row of colourful pencils pointing inward"></div>

    <h1 class="headline">Bramble Wren</h1>
    <div class="mark" aria-hidden="true"></div>

    <div class="cloud cloud-hours">
      <svg viewBox="0 0 210 122" aria-hidden="true">
        <path d="M44 110 C18 110 8 86 24 70 C10 52 30 30 54 38 C60 14 96 6 114 26 C132 8 170 18 168 46 C196 46 206 76 186 92 C192 108 176 116 160 110 Z"
              fill="#ffffff" stroke="#13aee8" stroke-width="2.5"/>
      </svg>
      <p>7:30am-<br>5:30pm</p>
    </div>
    <div class="cloud cloud-ages">
      <svg viewBox="0 0 210 122" aria-hidden="true">
        <path d="M44 110 C18 110 8 86 24 70 C10 52 30 30 54 38 C60 14 96 6 114 26 C132 8 170 18 168 46 C196 46 206 76 186 92 C192 108 176 116 160 110 Z"
              fill="#ffffff" stroke="#13aee8" stroke-width="2.5"/>
      </svg>
      <p>0 - 6<br>years old</p>
    </div>

    <h2 class="title">CHILDCARE</h2>
    <div class="phone">02 5550 1427</div>
  </section>
</div>
</body>
</html>
```